Poster Board Design

Hello.
This is what we will need on the design
Photo of truck
Company logo
Website: Bluerivoxfreightlines.com

Train Here... Drive here
$2,600 Weekly Average
Text/ Call: 428-555-7302
Must fit poster board size of 10'5"x 22'8"

i sent it via email reply idk how to send the photo in this box

```html
<!DOCTYPE html>
<html lang="en">
<head>
<meta charset="utf-8">
<title>Bluerivox Freight Lines – Poster Board</title>
<link rel="stylesheet" href="https://fonts.googleapis.com/css2?family=Montserrat:wght@500;600;700;800;900&display=swap">
<style>
  :root {
    --red: #be1e2d;
    --ink: #1b1b1b;
    --navy: #1f2a4a;
    --white: #ffffff;
    --panel-light: #f7f7f7;
    --panel-grey: #e4e4e4;
    --page: #ececec;
    --sky: #3f78c4;
    --sky-light: #8fb3de;
    --sand: #c9b59a;
  }
  * { margin: 0; padding: 0; box-sizing: border-box; }
  html, body {
    width: 931px;
    height: 1200px;
    overflow: hidden;
    background: var(--page);
    font-family: "Montserrat", sans-serif;
  }
  .poster {
    position: absolute;
    left: 30px;
    top: 400px;
    width: 871px;
    height: 400px;
    overflow: hidden;
    background: linear-gradient(135deg, var(--panel-grey) 0%, var(--panel-light) 45%, var(--white) 70%, var(--panel-light) 100%);
    box-shadow: 0 14px 28px rgba(0,0,0,0.28);
  }
  .poster__frame { position: absolute; inset: 0; }
  .brand {
    position: absolute;
    left: 53px;
    top: 62px;
    display: flex;
    align-items: center;
    gap: 12px;
    color: var(--ink);
    font-weight: 500;
  }
  .brand__mark {
    width: 16px;
    height: 16px;
    background: var(--red);
  }
  .brand__name {
    font-size: 21px;
    line-height: 1.25;
    letter-spacing: 0.06em;
  }
  .brand__name span { display: block; font-size: 14px; letter-spacing: 0.42em; }
  .headline {
    position: absolute;
    left: 53px;
    top: 192px;
    font-weight: 900;
    font-size: 38px;
    line-height: 1.12;
    letter-spacing: -0.01em;
  }
  .headline__train { color: var(--red); display: block; }
  .headline__drive { color: var(--ink); display: block; }
  .pay {
    position: absolute;
    left: 53px;
    top: 300px;
    height: 48px;
    display: flex;
  }
  .pay__amount {
    width: 196px;
    background: var(--red);
    color: var(--white);
    font-weight: 800;
    font-size: 36px;
    display: flex;
    align-items: center;
    justify-content: center;
    clip-path: polygon(0 0, 100% 0, 94% 100%, 0 100%);
  }
  .pay__label {
    margin-left: -8px;
    width: 152px;
    background: var(--ink);
    color: var(--white);
    font-weight: 800;
    font-size: 14px;
    line-height: 1.05;
    letter-spacing: 0.08em;
    display: flex;
    flex-direction: column;
    align-items: center;
    justify-content: center;
    clip-path: polygon(8% 0, 100% 0, 92% 100%, 0 100%);
  }
  .website {
    position: absolute;
    left: 53px;
    top: 364px;
    font-size: 13px;
    font-weight: 600;
    letter-spacing: 0.09em;
    color: var(--ink);
  }
  .website b { color: var(--red); font-weight: 600; }
  .contact {
    position: absolute;
    left: 430px;
    right: 0;
    top: 343px;
    height: 57px;
    display: flex;
    align-items: center;
    justify-content: center;
    color: var(--white);
    font-weight: 800;
    font-size: 25px;
  }
</style>
</head>
<body>
  <main class="poster">
    <svg class="poster__frame" width="871" height="400" viewBox="0 0 871 400">
      <defs>
        <linearGradient id="truck-photo-tone" x1="0" y1="0" x2="0" y2="1">
          <stop offset="0" stop-color="var(--sky)"/>
          <stop offset="0.55" stop-color="var(--sky-light)"/>
          <stop offset="0.7" stop-color="#a9a9a9"/>
          <stop offset="1" stop-color="var(--sand)"/>
        </linearGradient>
      </defs>
      <polygon class="photo-area" role="img" aria-label="Photo of a grey company semi truck driving on a dusty desert road under a blue sky"
               points="470,0 871,0 871,343 430,343 500,170" fill="url(#truck-photo-tone)"/>
      <polygon class="edge-shadow" points="436,6 468,6 498,172 428,343 420,343 486,172" fill="var(--navy)"/>
      <polygon class="edge-band" points="430,0 470,0 500,170 430,343 398,343 466,170" fill="var(--red)"/>
      <polygon class="contact-band" points="398,343 871,343 871,400 376,400" fill="var(--red)"/>
      <polygon class="contact-band-shadow" points="372,400 394,343 400,343 380,400" fill="var(--navy)"/>
    </svg>

    <div class="brand">
      <div class="brand__mark"></div>
      <div class="brand__name">BLUERIVOX<span>FREIGHT LINES</span></div>
    </div>

    <h1 class="headline">
      <span class="headline__train">TRAIN HERE...</span>
      <span class="headline__drive">DRIVE HERE</span>
    </h1>

    <div class="pay">
      <div class="pay__amount">$2,600</div>
      <div class="pay__label"><span>WEEKLY</span><span>AVERAGE</span></div>
    </div>

    <p class="website">www.<b>Bluerivoxfreightlines</b>.com</p>

    <p class="contact">Text / Call: 428-555-7302</p>
  </main>
</body>
</html>
```